Decking and Wooden Fencing Specialist Flyer Design

We are starting a new company offering decking installation, patios and wooden/stone fencing. We are looking for a flyer that gives professional impression, with an accent put on a high quality of services.

Industry/Entity Type

Fencing

```html
<!DOCTYPE html>
<html lang="en">
<head>
<meta charset="utf-8">
<title>Oakline Building Services – Decking and Wooden Fencing Specialist</title>
<link rel="stylesheet" href="https://fonts.googleapis.com/css2?family=Oswald:wght@400;500&family=Open+Sans:wght@400;600&display=swap">
<style>
  :root {
    --backdrop: #ededed;
    --paper: #ffffff;
    --bark: #3e2c1f;
    --wood-light: #efdcb6;
    --wood-mid: #dcbf8c;
    --teal: #4f8c8d;
    --ink: #1d1a17;
    --cream: #f4e3c2;
    --stone: #8c8170;
    --pebble: #9a9a96;
    --garden: #7f8f6a;
    --patio: #b9a88c;
    --deck: #a89784;
    --deck-board: #b5a794;
  }
  * { box-sizing: border-box; margin: 0; padding: 0; }
  html, body { width: 1200px; height: 962px; overflow: hidden; }
  body { background: var(--backdrop); position: relative; font-family: "Open Sans", sans-serif; }

  .flyer {
    position: absolute; background: var(--paper); overflow: hidden;
    box-shadow: 3px 4px 8px rgba(0,0,0,.25);
  }
  .flyer--portfolio { left: 57px; top: 57px; width: 511px; height: 664px; }
  .flyer--cover { left: 603px; top: 193px; width: 516px; height: 662px; }

  .block { position: absolute; }
  .photo { position: absolute; }
  .wood { background: linear-gradient(100deg, var(--wood-light) 0%, var(--wood-mid) 45%, var(--wood-light) 75%, var(--wood-mid) 100%); }
  .bark { background: var(--bark); }
  .teal { background: var(--teal); }

  .headline { font-family: "Oswald", sans-serif; color: var(--cream); line-height: 1; text-align: right; }
  .headline .big { display: block; font-weight: 400; }
  .headline .small-and { font-size: .72em; }
  .headline .tag { display: block; font-family: "Open Sans", sans-serif; color: #fff; letter-spacing: .02em; }

  .brand { font-family: "Oswald", sans-serif; color: var(--ink); font-weight: 500; white-space: nowrap; }

  .swatch { position: absolute; border-radius: 50%; border: 2px solid #fff; }
  .swatch--stone { background: radial-gradient(circle at 40% 35%, #a99d88, var(--stone)); }
  .swatch--wood { background: radial-gradient(circle at 40% 35%, #f1d7a8, #d8b57e); }
  .swatch--pebble { background: radial-gradient(circle at 40% 35%, #c2c2be, var(--pebble)); }

  .contact { position: absolute; display: flex; align-items: center; gap: 6px; color: #fff; font-size: 9px; }
  .contact svg { width: 11px; height: 11px; flex: none; }

  /* portfolio flyer */
  .p-hero { left: 0; top: 0; width: 349px; height: 262px; background: linear-gradient(160deg, #6f8d5f 0%, #a0623d 45%, #8f8a7e 100%); }
  .p-panel { left: 349px; top: 0; width: 162px; height: 262px; }
  .p-panel .headline { position: absolute; right: 12px; top: 20px; font-size: 33px; }
  .p-panel .headline .tag { font-size: 12px; margin-top: 8px; }
  .p-brandbar { left: 0; top: 270px; width: 343px; height: 70px; display: flex; align-items: center; justify-content: center; }
  .p-brandbar .brand { font-size: 32px; }
  .p-offer { left: 359px; top: 268px; width: 150px; font-size: 11px; line-height: 1.25; color: #3a3a3a; }
  .p-offer strong { display: block; font-weight: 600; }
  .p-offer ul { list-style: none; }
  .p-offer li::before { content: "• "; }
  .p-stripe { left: 0; top: 346px; width: 343px; height: 28px; }
  .p-patio { left: 0; top: 374px; width: 344px; height: 267px; background: linear-gradient(170deg, #a8b79b 0%, var(--garden) 30%, var(--patio) 55%, #c9b89c 100%); }
  .p-pebbles { left: 346px; top: 533px; width: 165px; height: 108px; background: linear-gradient(160deg, #d8d7d2, var(--pebble)); }
  .p-footer { left: 0; top: 641px; width: 511px; height: 23px; }

  /* cover flyer */
  .c-brandbar { left: 0; top: 0; width: 516px; height: 85px; display: flex; align-items: center; justify-content: center; }
  .c-brandbar .brand { font-size: 37px; }
  .c-panel { left: 0; top: 85px; width: 516px; height: 243px; }
  .c-panel .headline { position: absolute; right: 40px; top: 26px; font-size: 68px; }
  .c-panel .headline .big + .big { margin-top: 6px; }
  .c-panel .headline .tag { font-size: 25px; margin-top: 14px; }
  .c-garden { left: 0; top: 328px; width: 351px; height: 334px; background: linear-gradient(180deg, #7c8a86 0%, #6f7f52 35%, #7ea35a 50%, var(--deck) 70%, #b3a592 100%); }
  .c-planks { left: 351px; top: 328px; width: 165px; height: 334px; background: linear-gradient(170deg, #bfb19f 0%, var(--deck-board) 55%, #a5968a 100%); }
  .c-quality { left: 0; top: 601px; width: 348px; height: 42px; display: flex; align-items: center; padding-left: 22px; font-family: "Open Sans", sans-serif; color: #fff; font-size: 22px; letter-spacing: .01em; }
  .c-phone { left: 360px; top: 612px; color: var(--ink); font-size: 15px; }
  .c-phone svg { width: 15px; height: 15px; }
</style>
</head>
<body>

<article class="flyer flyer--portfolio">
  <div class="photo p-hero" role="img" aria-label="Garden with horizontal slatted timber fence, lit decking, potted plants and a tree"></div>

  <div class="block p-panel bark">
    <h2 class="headline">
      <span class="big">Decking</span>
      <span class="big"><span class="small-and">and</span> Wooden</span>
      <span class="tag">FENCING SPECIALIST</span>
    </h2>
    <div class="contact" style="left:12px; top:220px;">
      <svg viewBox="0 0 12 12" fill="none" stroke="#fff" stroke-width="1.2"><path d="M1 6 6 1.5 11 6M2.5 5v5.5h7V5"/></svg>
      <span>oaklinebuild@mail.com</span>
    </div>
    <div class="contact" style="left:38px; top:240px;">
      <svg viewBox="0 0 12 12" fill="none" stroke="#fff" stroke-width="1.3"><path d="M3 1.5c-1.5 1-1.5 3 0 5.5s3.5 4.5 5.5 4l1-1.5-2-1.5-1 .8C5.5 8 4.5 6.8 4 5.5l.9-.9L4 2z"/></svg>
      <span>07700918346</span>
    </div>
  </div>

  <div class="block p-brandbar wood"><span class="brand">Oakline Building Services</span></div>

  <div class="block p-offer">
    <strong>We offer:</strong>
    <ul>
      <li>decking installation</li>
      <li>patios and</li>
      <li>wooden/stone fencing</li>
    </ul>
  </div>

  <div class="block p-stripe teal"></div>
  <div class="photo p-patio" role="img" aria-label="Stone patio with a round fire pit, low stone wall and cushioned garden chairs"></div>

  <div class="swatch swatch--stone" role="img" aria-label="Stacked stone sample" style="left:404px; top:376px; width:54px; height:54px;"></div>
  <div class="swatch swatch--wood" role="img" aria-label="Light wood sample" style="left:404px; top:430px; width:54px; height:54px;"></div>
  <div class="swatch swatch--pebble" role="img" aria-label="Grey pebbles sample" style="left:404px; top:484px; width:54px; height:54px;"></div>

  <div class="photo p-pebbles" role="img" aria-label="Smooth grey pebbles"></div>
  <div class="block p-footer teal"></div>
</article>

<article class="flyer flyer--cover">
  <div class="block c-brandbar wood"><span class="brand">Oakline Building Services</span></div>

  <div class="block c-panel bark">
    <h1 class="headline">
      <span class="big">Decking</span>
      <span class="big"><span class="small-and">and</span> Wooden</span>
      <span class="tag">FENCING SPECIALIST</span>
    </h1>
  </div>

  <div class="photo c-garden" role="img" aria-label="Back garden with timber fence, raised sleeper beds, lawn, gravel path and decking"></div>
  <div class="photo c-planks" role="img" aria-label="Weathered timber decking boards"></div>

  <div class="swatch swatch--stone" role="img" aria-label="Stacked stone sample" style="left:404px; top:372px; width:70px; height:70px;"></div>
  <div class="swatch swatch--wood" role="img" aria-label="Light wood sample" style="left:404px; top:444px; width:70px; height:70px;"></div>
  <div class="swatch swatch--pebble" role="img" aria-label="Grey pebbles sample" style="left:404px; top:516px; width:70px; height:70px;"></div>

  <div class="block c-quality teal">HIGH QUALITY SERVICE</div>
  <div class="contact c-phone">
    <svg viewBox="0 0 12 12" fill="none" stroke="#1d1a17" stroke-width="1.3"><path d="M3 1.5c-1.5 1-1.5 3 0 5.5s3.5 4.5 5.5 4l1-1.5-2-1.5-1 .8C5.5 8 4.5 6.8 4 5.5l.9-.9L4 2z"/></svg>
    <span>07700918346</span>
  </div>
</article>

</body>
</html>
```